The Balanced Plate Hour with Dan Orrick.

I'm launching this podcast on health and wellness and I want to be take serious. That starts with a great design. There's too much contradiction out there about what is and isn't healthy. I want my podcast to be a resource that people can rely upon. I want my face in it and I want it to pop with colors that catch the eye. I want It clean and crisp. I was also thinking of experimenting with an animated photo of me as well. What ever looks best.

Industry/Entity Type

Health And Wellness

Font styles to use
Sans Serif

Requirements
Must have
• My face and or body.

```html
<!DOCTYPE html>
<html lang="en">
<head>
<meta charset="utf-8">
<title>The Balanced Plate Hour with Dan Orrick</title>
<link href="https://fonts.googleapis.com/css2?family=Archivo+Black&family=Oswald:wght@300&display=swap" rel="stylesheet">
<style>
  :root {
    --sun-edge: #d2c12c;
    --sun-core: #f3d170;
    --teal: #1a8070;
    --teal-deep: #12604f;
    --white: #ffffff;
    --navy: #0d2466;
    --navy-light: #1c3f80;
    --photo-red: #d81f26;
    --photo-orange: #dc6a28;
    --photo-lime: #b9bf22;
    --photo-outline: #f6d98a;
  }
  html, body {
    margin: 0;
    padding: 0;
    width: 1200px;
    height: 1200px;
    overflow: hidden;
  }
  .cover {
    position: relative;
    width: 1200px;
    height: 1200px;
    background: radial-gradient(circle at 40% 55%, var(--sun-core) 0%, var(--sun-core) 42%, var(--sun-edge) 100%);
    overflow: hidden;
  }
  .cover-art {
    position: absolute;
    inset: 0;
  }
  .title-line {
    font-family: "Archivo Black", "Arial Black", sans-serif;
    fill: var(--white);
  }
  .host-line {
    font-family: "Oswald", "Arial Narrow", sans-serif;
    font-weight: 300;
    fill: var(--white);
    letter-spacing: 6px;
  }
</style>
</head>
<body>
<div class="cover">
  <svg class="cover-art" width="1200" height="1200" viewBox="0 0 1200 1200" xmlns="http://www.w3.org/2000/svg">
    <defs>
      <linearGradient id="tealShade" x1="0" y1="0" x2="1" y2="1">
        <stop offset="0" stop-color="var(--teal)"/>
        <stop offset="0.75" stop-color="var(--teal)"/>
        <stop offset="1" stop-color="var(--teal-deep)"/>
      </linearGradient>
      <linearGradient id="hostTone" x1="0.2" y1="0" x2="0.8" y2="1">
        <stop offset="0" stop-color="var(--photo-red)"/>
        <stop offset="0.45" stop-color="var(--photo-orange)"/>
        <stop offset="1" stop-color="var(--photo-lime)"/>
      </linearGradient>
      <linearGradient id="micTone" x1="0" y1="0" x2="0" y2="1">
        <stop offset="0" stop-color="var(--navy-light)"/>
        <stop offset="1" stop-color="var(--navy)"/>
      </linearGradient>
    </defs>

    <polygon class="long-shadow" fill="url(#tealShade)"
      points="520,70 740,70 850,188 1080,188 1200,322 1200,1200 830,1200 520,860 250,560 250,326 200,310 200,188 520,188"/>

    <path class="host-photo" role="img" aria-label="Photo of host Dan Orrick, shirtless and smiling, in a red-to-lime duotone"
      fill="url(#hostTone)" stroke="var(--photo-outline)" stroke-width="5"
      d="M256,590 C300,540 380,525 440,540 C500,560 530,610 528,680 C526,740 520,790 505,840 C560,880 640,920 700,980 C760,1050 800,1120 820,1200 L0,1200 L0,1060 C60,1030 130,1010 200,990 C230,940 250,860 238,790 C215,770 220,720 240,720 C235,680 235,630 256,590 Z"/>

    <rect class="mic-illustration" role="img" aria-label="Illustration of a vintage microphone with lightning bolts"
      x="780" y="860" width="152" height="340" rx="44" fill="url(#micTone)" stroke="#f3ead0" stroke-width="4"/>

    <text class="title-line" x="520" y="156" font-size="104" textLength="212" lengthAdjust="spacingAndGlyphs">THE</text>
    <text class="title-line" x="200" y="310" font-size="170" textLength="880" lengthAdjust="spacingAndGlyphs">BALANCED</text>
    <text class="title-line" x="250" y="470" font-size="200" textLength="760" lengthAdjust="spacingAndGlyphs">PLATE</text>
    <text class="title-line" x="590" y="612" font-size="150" textLength="420" lengthAdjust="spacingAndGlyphs">HOUR</text>
    <text class="host-line" x="628" y="690" font-size="52" textLength="344" lengthAdjust="spacing">WITH DAN ORRICK</text>
  </svg>
</div>
</body>
</html>
```